Executive Business Card for Healthcare Company [Need Today]

I need a business card design for a healthcare company. The only branding the company has thus far is a logo. The cards will be utilized by company executives. The design I envision will be vibrant and appealing but with a corporate feel. They shouldn't be too casual or playful. I would like to complete this project TODAY if possible.

Target Market(s)

Healthcare vendors, other executives in healthcare and pharmaceuticals

Industry/Entity Type

Pharmaceutical

Contact Information for Business Card

See attachment

Font styles to use
Serif
Sans Serif

Colors

Designer to choose colors to be used in the design.

```html
<!DOCTYPE html>
<html lang="en">
<head>
<meta charset="utf-8">
<title>Corvane Therapeutics — Business Card</title>
<link href="https://fonts.googleapis.com/css2?family=Questrial&display=swap" rel="stylesheet">
<style>
  :root {
    --teal: #35bfc6;
    --teal-text: #2fb6bf;
    --green-ring: #5cbf8e;
    --grey-band: #7a7a7a;
    --ink: #555555;
    --paper: #ffffff;
    --stage: #2a2a2a;
  }
  * { margin: 0; padding: 0; box-sizing: border-box; }
  html, body { width: 1200px; height: 1189px; overflow: hidden; }
  body {
    background: var(--stage);
    font-family: "Questrial", "Century Gothic", sans-serif;
    position: relative;
  }
  .card {
    position: absolute;
    left: 170px;
    width: 860px;
    height: 491px;
    border-radius: 34px;
    overflow: hidden;
  }
  .card-front { top: 70px; background: var(--teal); }
  .card-back { top: 628px; background: var(--paper); }

  .front-ring {
    position: absolute;
    left: -120px; top: 120px;
    width: 420px; height: 420px;
    border: 14px solid rgba(255,255,255,0.18);
    border-radius: 50%;
  }
  .brand {
    position: absolute;
    display: flex;
    align-items: center;
    gap: 22px;
  }
  .brand-mark {
    border-radius: 50%;
    flex: none;
  }
  .brand-name {
    font-size: 44px;
    line-height: 1.05;
    letter-spacing: 0.5px;
  }
  .card-front .brand { left: 250px; top: 186px; }
  .card-front .brand-mark { width: 112px; height: 112px; border: 4px solid var(--paper); }
  .card-front .brand-name { color: var(--paper); }

  .card-back .brand { left: 58px; top: 46px; }
  .card-back .brand-mark { width: 104px; height: 104px; border: 4px solid var(--green-ring); }
  .card-back .brand-name { color: var(--teal-text); }

  .swoosh { position: absolute; inset: 0; width: 860px; height: 491px; }

  .person { position: absolute; left: 92px; top: 300px; width: 340px; }
  .person-name { color: var(--teal-text); font-size: 27px; }
  .person-title { color: var(--ink); font-size: 20px; margin-top: 2px; }
  .rule { height: 1.5px; background: var(--teal); margin: 14px 0 12px; }
  .contacts { list-style: none; }
  .contacts li {
    display: flex; align-items: center; gap: 12px;
    color: var(--ink); font-size: 21px; line-height: 31px;
  }
  .icon { width: 20px; height: 20px; flex: none; }

  .company { position: absolute; left: 470px; top: 272px; width: 250px; }
  .company .rule { margin: 0 0 10px; }
  .company-name { color: var(--teal-text); font-size: 20px; }
  .company-address { color: var(--ink); font-size: 19px; line-height: 25px; }
</style>
</head>
<body>

<section class="card card-front">
  <div class="front-ring"></div>
  <div class="brand">
    <span class="brand-mark"></span>
    <span class="brand-name">corvane<br>therapeutics</span>
  </div>
</section>

<section class="card card-back">
  <svg class="swoosh" viewBox="0 0 860 491" aria-hidden="true">
    <path d="M655 0 C720 130 720 300 790 491 L860 491 L860 0 Z" fill="var(--grey-band)"/>
    <path d="M675 0 C740 130 740 300 808 491 L860 491 L860 0 Z" fill="var(--paper)"/>
    <path d="M690 0 C755 130 755 300 822 491 L860 491 L860 0 Z" fill="var(--teal)"/>
  </svg>

  <div class="brand">
    <span class="brand-mark"></span>
    <span class="brand-name">corvane<br>therapeutics</span>
  </div>

  <div class="person">
    <p class="person-name">Daniel Marsh</p>
    <p class="person-title">Senior Director of Marketing</p>
    <div class="rule"></div>
    <ul class="contacts">
      <li>
        <svg class="icon" viewBox="0 0 20 20"><circle cx="10" cy="10" r="9" fill="none" stroke="var(--green-ring)" stroke-width="1.6"/><rect x="7" y="5" width="6" height="10" rx="1" fill="none" stroke="var(--green-ring)" stroke-width="1.4"/></svg>
        555-214-0387
      </li>
      <li>
        <svg class="icon" viewBox="0 0 20 20"><circle cx="10" cy="10" r="9" fill="var(--green-ring)"/><path d="M5 9 Q10 5 15 9 L13.5 10.5 L12 9.5 L8 9.5 L6.5 10.5 Z M7 11 H13 L14 14 H6 Z" fill="var(--paper)"/></svg>
        555-760-1142
      </li>
      <li>
        <svg class="icon" viewBox="0 0 20 20"><circle cx="10" cy="10" r="9" fill="var(--green-ring)"/><rect x="5" y="6.5" width="10" height="7" fill="var(--paper)"/><path d="M5 6.5 L10 11 L15 6.5" fill="none" stroke="var(--green-ring)" stroke-width="1.2"/></svg>
        dmarsh@corvanerx.com
      </li>
    </ul>
  </div>

  <div class="company">
    <div class="rule"></div>
    <p class="company-name">Corvane Therapeutics, LLC</p>
    <p class="company-address">118 W Meridian Avenue<br>Fairview, GA 30999</p>
  </div>
</section>

</body>
</html>
```